Fun relaxed Travel Photography Business Card*

Require a fun, funky and quirky but rememberable business card for a travel photographer

Industry/Entity Type

Photographer

Contact Information for Business Card

Front Card

(my name) Dane M.

Travel Photographer ( small under travel photographer) “self-proclaimed”

(website logo) wanderingsofdane.example

(Instagram logo) @wanderings_of_dane

(Instagram logo) @wanderings_of_dane_2.0 (backup for when Instagram puts Dane on timeout for bad behaviour)

Tel: N/A (removing the potential awkwardness of me not replying)

Email: (see above)

Back Card

Offending people since 1986

(Bottom right corner) “p.s. travelling made me fatTER”

Font styles to use
Serif

Colors

Designer to choose colors to be used in the design.

Requirements
Must have
• a camera
• a similar cartoon version of me as the "logo" see attached files, try to make as similar as possible

```html
<!DOCTYPE html>
<html lang="en">
<head>
<meta charset="utf-8">
<title>Dane M. – Travel Photographer Business Card</title>
<link rel="stylesheet" href="https://fonts.googleapis.com/css2?family=PT+Serif:wght@400;700&display=swap">
<style>
  :root {
    --backdrop: #34343a;
    --card: #1e1e21;
    --card-pattern: #262629;
    --ink: #f2f2f2;
    --ink-soft: #d6d6d6;
    --rule: #8a8a8a;
  }
  * { box-sizing: border-box; margin: 0; padding: 0; }
  html, body {
    width: 1200px;
    height: 1108px;
    overflow: hidden;
    background: var(--backdrop);
    font-family: "PT Serif", serif;
    color: var(--ink);
  }
  .stage {
    position: relative;
    width: 1200px;
    height: 1108px;
  }
  .card {
    position: absolute;
    top: 234px;
    width: 390px;
    height: 640px;
    background: var(--card);
    border-radius: 22px;
    box-shadow: 0 18px 40px rgba(0,0,0,0.45);
    overflow: hidden;
  }
  .card--front { left: 170px; }
  .card--back { left: 640px; }

  /* Front */
  .identity {
    position: absolute;
    top: 130px;
    left: 0;
    width: 100%;
    display: flex;
    justify-content: center;
    align-items: flex-start;
    gap: 14px;
  }
  .identity__mark {
    width: 58px;
    height: 58px;
    margin-top: 8px;
    border: 3px solid var(--ink);
    border-radius: 6px;
    flex: none;
  }
  .identity__text {
    display: flex;
    flex-direction: column;
    align-items: flex-end;
  }
  .identity__name {
    font-size: 60px;
    font-weight: 400;
    line-height: 1;
    align-self: flex-start;
  }
  .identity__title {
    margin-top: 8px;
    font-size: 15px;
    font-weight: 700;
    letter-spacing: 1.5px;
    text-transform: uppercase;
  }
  .identity__note {
    font-size: 9px;
    font-weight: 700;
    letter-spacing: 1.5px;
    text-transform: uppercase;
    margin-top: 2px;
    padding-bottom: 5px;
    border-bottom: 3px solid var(--ink);
    width: 150px;
    text-align: center;
  }
  .divider {
    position: absolute;
    left: 45px;
    width: 300px;
    height: 30px;
    display: flex;
    align-items: center;
    justify-content: center;
    gap: 6px;
  }
  .divider::before, .divider::after {
    content: "";
    flex: 1;
    height: 1px;
    background: var(--rule);
  }
  .divider--contact { top: 382px; }
  .divider--social { top: 494px; }
  .icon-dot {
    width: 22px;
    height: 22px;
    border-radius: 50%;
    background: var(--ink);
    display: flex;
    align-items: center;
    justify-content: center;
  }
  .icon-dot svg { width: 13px; height: 13px; }
  .contact-list, .social-list {
    position: absolute;
    left: 0;
    width: 100%;
    list-style: none;
    text-align: center;
    font-size: 18px;
    line-height: 27px;
    color: var(--ink-soft);
  }
  .contact-list { top: 416px; }
  .social-list { top: 528px; }

  /* Back */
  .pattern-field {
    position: absolute;
    top: 0;
    left: 0;
    width: 100%;
    height: 440px;
    background: linear-gradient(180deg, var(--card-pattern) 0%, var(--card-pattern) 70%, var(--card) 100%);
  }
  .back-mark {
    position: absolute;
    top: 296px;
    left: 0;
    width: 100%;
    display: flex;
    justify-content: center;
    align-items: center;
    gap: 10px;
    font-size: 26px;
  }
  .back-mark__square {
    width: 34px;
    height: 34px;
    border: 2px solid var(--ink);
    border-radius: 4px;
  }
  .back-lines {
    position: absolute;
    top: 462px;
    left: 0;
    width: 100%;
    text-align: center;
    list-style: none;
    font-size: 17px;
    line-height: 22px;
    text-transform: uppercase;
    color: var(--ink-soft);
  }
  .back-lines li + li { margin-top: 24px; }
</style>
</head>
<body>
<main class="stage">
  <section class="card card--front" aria-label="Front of card">
    <header class="identity">
      <span class="identity__mark" aria-hidden="true"></span>
      <div class="identity__text">
        <h1 class="identity__name">Dane M.</h1>
        <span class="identity__title">Travel Photographer</span>
        <span class="identity__note">Self-proclaimed</span>
      </div>
    </header>

    <div class="divider divider--contact">
      <span class="icon-dot" aria-label="Email">
        <svg viewBox="0 0 16 16"><rect x="1.5" y="3.5" width="13" height="9" fill="none" stroke="var(--card)" stroke-width="1.6"/><path d="M1.5 3.5 8 9l6.5-5.5" fill="none" stroke="var(--card)" stroke-width="1.6"/></svg>
      </span>
      <span class="icon-dot" aria-label="Website">
        <svg viewBox="0 0 16 16"><circle cx="8" cy="8" r="6" fill="none" stroke="var(--card)" stroke-width="1.5"/><ellipse cx="8" cy="8" rx="2.5" ry="6" fill="none" stroke="var(--card)" stroke-width="1.2"/><path d="M2 8h12" stroke="var(--card)" stroke-width="1.2"/></svg>
      </span>
    </div>
    <ul class="contact-list">
      <li>info@wanderingsofdane.example</li>
      <li>www.wanderingsofdane.example</li>
    </ul>

    <div class="divider divider--social">
      <span class="icon-dot" aria-label="Social handle"></span>
    </div>
    <ul class="social-list">
      <li>@wanderings_of_dane</li>
      <li>@wanderings_of_dane_2.0</li>
    </ul>
  </section>

  <section class="card card--back" aria-label="Back of card">
    <div class="pattern-field" role="img" aria-label="Faint repeating pattern of the camera logo mark"></div>
    <p class="back-mark"><span class="back-mark__square" aria-hidden="true"></span>Dane M.</p>
    <ul class="back-lines">
      <li>Offending people since 1986</li>
      <li>P.S. Travelling made me fatter</li>
    </ul>
  </section>
</main>
</body>
</html>
```